Peltrix – Nimbara Flyer for Brivella (Halvern Travel Corporation)

Overview
Halvern Travel Corporation is launching a series of branded flyers to highlight the features and benefits of our Peltrix platform — our all-in-one corporate travel technology suite.
This first flyer will spotlight Nimbara, our risk management and traveller safety solution, and will be published on Brivella as part of a digital awareness campaign.
⸻
Objective
Create a striking, professional, and modern flyer that communicates how Nimbara enhances the Peltrix platform by ensuring traveller safety, communication, and real-time updates.
The design should feel premium, contemporary, and aligned with Halvern Travel’s luxury corporate identity.
⸻
Target Audience
• Corporate clients and travel decision-makers
• Travel managers, procurement teams, and executive assistants
• Existing Halvern Travel corporate partners on Brivella
⸻
Key Message
Nimbara – Your travellers’ safety, visibility, and communication, all in one place.
Part of Peltrix, Halvern Travel’s integrated corporate travel platform.
⸻
Core Features to Highlight
• 24/7 real-time risk alerts
• Instant traveller identification and tracking by location or timeframe
• Two-way communication between traveller and company
• Integrated with travel itineraries for seamless care
• Supports duty-of-care compliance for corporate travel policies
⸻
Tone & Style
• Sophisticated, trusted, and innovative
• Clean lines, premium feel, and minimal clutter
• Should feel like a Halvern Travel-branded asset — not overly “techy”
• Imagery: travel safety, global maps, communication lines, or business travellers in motion
⸻
Design Direction
• Brand: Use Halvern Travel brand colours (gold, charcoal, white, navy)
• Typography: Professional, modern sans-serif fonts
• Logo: Include Halvern Travel and Peltrix logos (can supply if needed)
• CTA: “Discover Nimbara on Peltrix” or “Raise the Halvern Benchmark for Business Trips”
• Layout: Ideal for Brivella post format (square or 4:5 vertical)
⸻
Deliverables
• Editable design file (AI / PSD / InDesign)
• Final exports for social media:
• 1080x1080 px (Brivella square)
• 1080x1350 px (Brivella portrait)
• Include space for light text overlay (for post captioning later)
⸻
Inspiration
• Style similar to luxury tech or premium corporate innovation brands
• Feel: clean, high-contrast, aspirational, minimal

```html
<!DOCTYPE html>
<html lang="en">
<head>
<meta charset="UTF-8">
<title>Nimbara on Peltrix – Halvern Travel Corporation</title>
<link href="https://fonts.googleapis.com/css2?family=Montserrat:wght@500;600;700;800&display=swap" rel="stylesheet">
<style>
:root{
  --navy:#03183b;
  --gold:#dda25e;
  --gold-pale:#f6e3cc;
  --white:#ffffff;
  --mist:#e4e4e6;
  --sky:#2f9be6;
  --ink:#0b1a3a;
}
*{margin:0;padding:0;box-sizing:border-box}
html,body{width:1200px;height:1200px;overflow:hidden;background:var(--white)}
.flyer{position:relative;width:1200px;height:1200px;overflow:hidden;font-family:'Montserrat',sans-serif;background:var(--white)}
.backdrop-photo{position:absolute;left:0;top:560px;width:1200px;height:640px;
  background:linear-gradient(180deg,var(--white) 0%,#f1f1f2 25%,var(--mist) 70%,#d9d9db 100%)}
.shapes{position:absolute;left:0;top:0}
.brand{position:absolute;left:155px;top:36px;color:var(--gold);font-weight:800;line-height:1}
.brand-name{font-size:68px;letter-spacing:-2px}
.brand-sub{display:block;font-size:22px;margin-top:10px;letter-spacing:0.5px}
.headline{position:absolute;left:560px;top:158px;width:620px;color:var(--white);font-weight:600;font-size:46px;line-height:51px}
.headline .product{color:var(--gold);font-weight:700}
.platform-note{position:absolute;left:560px;top:430px;color:var(--ink);font-weight:600;font-size:27px;line-height:35px}
.cta-pill{position:absolute;left:0;top:621px;width:472px;height:63px;background:var(--navy);
  border-radius:0 32px 32px 0;box-shadow:4px 4px 0 var(--white),6px 8px 14px rgba(0,0,0,.25);
  color:var(--white);font-weight:700;font-size:34px;line-height:63px;padding-left:92px}
.cta-pill .product{color:var(--gold)}
.cta-on{position:absolute;left:92px;top:694px;color:var(--ink);font-weight:500;font-size:24px}
.cta-on .platform{color:var(--sky);font-size:30px;font-weight:600}
.features{position:absolute;left:68px;top:760px;list-style:none;width:600px}
.features li{position:relative;padding-left:39px;color:var(--ink);font-weight:600;font-size:27px;line-height:35px;margin-bottom:14px}
.features li::before{content:"";position:absolute;left:0;top:10px;width:17px;height:17px;background:var(--gold)}
.traveller-photo{position:absolute;left:738px;top:688px;width:342px;height:342px;border-radius:50%;
  background:radial-gradient(circle at 50% 40%,#d9d2c4 0%,#b39a78 45%,#6b5a47 100%)}
</style>
</head>
<body>
<div class="flyer">
  <div class="backdrop-photo" role="img" aria-label="Faded view of an aircraft wing over a city seen from above"></div>

  <svg class="shapes" width="1200" height="1200" viewBox="0 0 1200 1200" aria-hidden="true">
    <defs>
      <linearGradient id="bandFade" x1="0" x2="1" y1="0" y2="0">
        <stop offset="0" stop-color="#dda25e" stop-opacity="0"/>
        <stop offset="0.35" stop-color="#dda25e" stop-opacity="0.55"/>
        <stop offset="0.7" stop-color="#dda25e"/>
        <stop offset="1" stop-color="#dda25e"/>
      </linearGradient>
    </defs>
    <rect class="note-band" x="340" y="411" width="860" height="106" fill="url(#bandFade)"/>
    <path class="gold-swoosh" fill="var(--gold)"
      d="M75,275 C110,400 230,500 400,565 C530,615 640,720 697,806 L712,760 C640,660 520,565 390,490 C250,410 130,350 75,275 Z"/>
    <path class="navy-swoosh" fill="var(--navy)"
      d="M72,0 C15,120 0,220 75,275 C150,360 300,440 430,522 C560,605 650,680 705,751 L716,735 C630,625 520,540 330,414 L330,392 L1200,392 L1200,0 Z"/>
    <path class="swoosh-line" fill="none" stroke="var(--white)" stroke-width="9"
      d="M82,0 C70,140 120,260 318,392"/>
    <path class="swoosh-edge" fill="none" stroke="var(--white)" stroke-width="6"
      d="M330,398 C500,505 630,610 720,730"/>
    <rect x="0" y="392" width="1200" height="19" fill="var(--white)"/>
    <line class="rule" x1="547" y1="121" x2="1158" y2="121" stroke="var(--gold)" stroke-width="1.5"/>
    <circle cx="909" cy="859" r="247" fill="var(--white)" opacity="0.55"/>
    <circle cx="909" cy="859" r="216" fill="var(--white)" stroke="var(--gold)" stroke-width="10"/>
    <circle cx="909" cy="859" r="180" fill="var(--navy)"/>
  </svg>

  <div class="brand">
    <span class="brand-name">Halvern</span>
    <span class="brand-sub">TRAVEL CORPORATION</span>
  </div>

  <h1 class="headline"><span class="product">Nimbara –</span> Your travellers’ safety, visibility, and communication, all in one place.</h1>

  <p class="platform-note">Part of Peltrix, Halvern Travel’s<br>integrated corporate travel platform.</p>

  <div class="cta-pill">Discover <span class="product">Nimbara</span></div>
  <p class="cta-on">on <span class="platform">Peltrix</span></p>

  <ul class="features">
    <li>24/7 real-time risk alerts</li>
    <li>Instant traveller identification and tracking by location or timeframe</li>
    <li>Two-way communication between traveller and company</li>
    <li>Integrated with travel itineraries for seamless care</li>
    <li>Supports duty-of-care compliance for corporate travel policies</li>
  </ul>

  <div class="traveller-photo" role="img" aria-label="Business traveller walking through an airport terminal with a rolling suitcase"></div>
</div>
</body>
</html>
```